Nordavexa - world unique technology for better life - please let them know who am i at first sight

We need a new business card for company which is a provider of unique crystal based technology suitable for all living being. For more information and final design you can use our brochure (our colours are black and blue from brochure).
We use Verdana font

Industry/Entity Type

Business

Contact Information for Business Card

regular dimension

Other font styles liked:
• Verdana

Requirements
Must have
• Logo
• name
• function/position
• phone
• mobile
• e-mail
• adress
Nice to have
• inovative design (technology directed)

```html
<!DOCTYPE html>
<html lang="en">
<head>
<meta charset="utf-8">
<title>Nordavexa Technologies – Business Card</title>
<link href="https://fonts.googleapis.com/css2?family=Open+Sans:wght@300;400;600&display=swap" rel="stylesheet">
<style>
  :root {
    --backdrop: #d9d4cc;
    --card-black: #07090b;
    --card-deep: #0b1418;
    --brand-blue: #2bb8e6;
    --brand-blue-soft: #1a7fa3;
    --text-light: #8fd6ef;
    --shadow: rgba(0, 0, 0, 0.35);
  }
  * { margin: 0; padding: 0; box-sizing: border-box; }
  html, body {
    width: 1200px;
    height: 1023px;
    overflow: hidden;
    background: var(--backdrop);
    font-family: "Open Sans", Verdana, sans-serif;
  }
  .canvas {
    position: relative;
    width: 1200px;
    height: 1023px;
  }
  .card {
    position: absolute;
    width: 600px;
    height: 343px;
    background: var(--card-black);
    border-radius: 4px;
    box-shadow: 0 18px 40px var(--shadow);
    overflow: hidden;
  }

  /* Front side */
  .card-front { left: 80px; top: 110px; }
  .front-texture {
    position: absolute;
    left: 0;
    top: 0;
    width: 300px;
    height: 343px;
    background:
      radial-gradient(ellipse at 30% 25%, rgba(43,184,230,0.85) 0%, rgba(43,184,230,0.25) 38%, transparent 62%),
      radial-gradient(ellipse at 80% 70%, rgba(43,184,230,0.8) 0%, rgba(43,184,230,0.2) 35%, transparent 60%);
  }
  .holder {
    position: absolute;
    left: 32px;
    bottom: 30px;
    color: var(--brand-blue);
    font-size: 17px;
    font-weight: 600;
    letter-spacing: 0.2px;
  }
  .holder .role {
    font-weight: 400;
    font-size: 13px;
    color: var(--text-light);
  }
  .contact-list {
    position: absolute;
    left: 330px;
    top: 44px;
    list-style: none;
  }
  .contact-list li {
    display: flex;
    align-items: center;
    gap: 10px;
    color: var(--text-light);
    font-size: 13px;
    line-height: 1;
    margin-bottom: 12px;
  }
  .icon {
    width: 16px;
    height: 16px;
    flex: none;
  }
  .address {
    position: absolute;
    left: 330px;
    top: 190px;
    display: flex;
    gap: 10px;
    color: var(--text-light);
    font-size: 13px;
    line-height: 1.55;
    font-style: normal;
  }
  .address .icon { margin-top: 2px; }

  /* Back side */
  .card-back {
    left: 520px;
    top: 570px;
    background: linear-gradient(135deg, var(--card-deep) 0%, var(--card-black) 70%);
  }
  .brand {
    position: absolute;
    left: 0;
    top: 0;
    width: 100%;
    height: 100%;
    display: flex;
    align-items: center;
    justify-content: center;
    gap: 18px;
  }
  .brand-dot {
    width: 62px;
    height: 62px;
    border-radius: 50%;
    background: var(--brand-blue);
  }
  .brand-words { color: var(--brand-blue); font-weight: 300; }
  .brand-name {
    font-size: 44px;
    letter-spacing: 2px;
    line-height: 1;
  }
  .brand-sub {
    font-size: 13px;
    letter-spacing: 11px;
    margin-top: 8px;
  }
</style>
</head>
<body>
<main class="canvas">

  <section class="card card-front" aria-label="Business card front">
    <div class="front-texture" role="img" aria-label="Blue crystal lattice decoration"></div>

    <p class="holder">Lena Marsh <span class="role">| Director</span></p>

    <ul class="contact-list">
      <li>
        <svg class="icon" viewBox="0 0 16 16" aria-hidden="true">
          <rect width="16" height="16" rx="3" fill="var(--brand-blue)"/>
          <path d="M5 3.5l1.6 2.3-1 1.2c.6 1.3 1.5 2.2 2.8 2.8l1.2-1 2.3 1.6-.8 1.8C7.6 12 4 8.4 3.7 4.3z" fill="var(--card-black)"/>
        </svg>
        +31 20 555 0184
      </li>
      <li>
        <svg class="icon" viewBox="0 0 16 16" aria-hidden="true">
          <rect width="16" height="16" rx="3" fill="var(--brand-blue)"/>
          <rect x="3.5" y="5" width="9" height="6.5" fill="none" stroke="var(--card-black)" stroke-width="1.3"/>
          <path d="M3.5 5l4.5 3.6L12.5 5" fill="none" stroke="var(--card-black)" stroke-width="1.3"/>
        </svg>
        info@nordavexatechnologies.com
      </li>
      <li>
        <svg class="icon" viewBox="0 0 16 16" aria-hidden="true">
          <rect width="16" height="16" rx="3" fill="var(--brand-blue)"/>
          <circle cx="8" cy="8" r="4.5" fill="none" stroke="var(--card-black)" stroke-width="1.2"/>
          <path d="M3.5 8h9M8 3.5c-2 2.4-2 6.6 0 9M8 3.5c2 2.4 2 6.6 0 9" fill="none" stroke="var(--card-black)" stroke-width="1"/>
        </svg>
        www.NORDAVEXAtechnologies.com
      </li>
    </ul>

    <address class="address">
      <svg class="icon" viewBox="0 0 16 16" aria-hidden="true">
        <rect width="16" height="16" rx="3" fill="var(--brand-blue)"/>
        <path d="M8 13s-3.5-3.6-3.5-6a3.5 3.5 0 017 0c0 2.4-3.5 6-3.5 6z" fill="var(--card-black)"/>
        <circle cx="8" cy="7" r="1.3" fill="var(--brand-blue)"/>
      </svg>
      <span>BV Lindengracht 48<br>1016 KX Amsterdam<br>The Netherlands</span>
    </address>
  </section>

  <section class="card card-back" aria-label="Business card back">
    <div class="brand">
      <span class="brand-dot" aria-hidden="true"></span>
      <div class="brand-words">
        <p class="brand-name">NORDAVEXA</p>
        <p class="brand-sub">TECHNOLOGIES</p>
      </div>
    </div>
  </section>

</main>
</body>
</html>
```